Web Design Project

Revamp current website adding newly designed logo and creating layout that is good on desktops, tablets, and cell phones.

Current website can be viewed at www.venkirainteriors.com

Will you see the website is small but graphics heavy in the gallery. The gallery needs to be setup so that it is easy to maintain the links and update the photos.

Needs to have high visual impact.

I need a new logo and website layout designed for my partner's business. This is a birthday present. His business is interior painting, wallpapering and design. He also has access to a wide variety of products including carpet, fabrics, furniture, wallpaper, tile, countertops, etc. I have attached some screen shots of his website for reference. He is a one man shop and has a stellar reputation with his customers. He is on-time, very tidy, excellent with animals, and always finishes on time and on budget. There are no restrictions on colors or fonts. The logo needs to work well with the website, business cards and printed materials. The website needs to flow content for device size so it looks just as good on a cell phone or tablet as it does on a desktop computer. Whatever the heck that's called! Thanks. I am looking forward to seeing everyone's ideas.

Target Market(s)

Consumers looking for interior design, painting, and wallpapering as well as interior products such as flooring, window treatments, reupholstering, counter tops, etc.

Industry/Entity Type

Cell Phone

Requirements
Must have
• Clean, sharp, visual impact (at least on the home page)
Should not have
• Clutter.

```html
<!DOCTYPE html>
<html lang="en">
<head>
<meta charset="utf-8">
<title>Venkira Interiors — Home</title>
<link rel="stylesheet" href="https://fonts.googleapis.com/css2?family=Libre+Baskerville:ital@1&family=Raleway:wght@300&family=Arimo:wght@400&display=swap">
<style>
  :root {
    --page-bg: #ffffff;
    --ink-navy: #1c1338;
    --accent-red: #7f1d1d;
    --accent-orange: #f39200;
    --panel-veil: rgba(255, 255, 255, 0.72);
    --photo-white: #f4f5f4;
    --photo-light: #dfe3e2;
    --photo-mid: #b9bfbd;
    --photo-dark: #6f7572;
    --photo-charcoal: #3b3f3e;
    --photo-wood: #cbbfae;
  }
  * { box-sizing: border-box; margin: 0; padding: 0; }
  html, body {
    width: 1200px;
    height: 638px;
    overflow: hidden;
    background: var(--page-bg);
  }
  .site {
    position: relative;
    width: 1200px;
    height: 638px;
  }
  .sidebar {
    position: absolute;
    left: 56px;
    top: 66px;
    width: 150px;
    text-align: center;
  }
  .brand {
    display: flex;
    flex-direction: column;
    align-items: center;
    justify-content: center;
    gap: 8px;
    height: 98px;
  }
  .brand-mark {
    width: 34px;
    height: 34px;
    background: var(--accent-red);
  }
  .brand-name {
    font-family: "Libre Baskerville", Georgia, serif;
    font-style: italic;
    font-size: 17px;
    color: var(--ink-navy);
    line-height: 1.2;
    white-space: nowrap;
  }
  .main-nav {
    list-style: none;
    margin-top: 26px;
  }
  .main-nav li {
    font-family: "Libre Baskerville", Georgia, serif;
    font-style: italic;
    font-size: 15px;
    line-height: 28px;
    color: var(--ink-navy);
  }
  .main-nav li.is-current { color: var(--accent-red); }
  .social-links {
    display: flex;
    justify-content: center;
    gap: 20px;
    margin-top: 40px;
  }
  .social-links span {
    width: 10px;
    height: 10px;
    border-radius: 50%;
    background: var(--accent-orange);
  }
  .hero {
    position: absolute;
    left: 226px;
    top: 66px;
    width: 844px;
    height: 506px;
    overflow: hidden;
  }
  .hero-photo {
    position: absolute;
    inset: 0;
    background:
      linear-gradient(180deg, rgba(120,126,124,0.55) 0%, rgba(255,255,255,0) 14%, rgba(255,255,255,0) 62%, rgba(255,255,255,0.55) 74%, rgba(203,191,174,0.9) 100%),
      linear-gradient(90deg, var(--photo-mid) 0%, var(--photo-dark) 4%, var(--photo-light) 11%, var(--photo-white) 24%, var(--photo-light) 40%, var(--photo-charcoal) 47%, var(--photo-mid) 55%, var(--photo-light) 68%, var(--photo-mid) 86%, var(--photo-dark) 95%, var(--photo-charcoal) 100%);
  }
  .welcome-panel {
    position: absolute;
    left: 403px;
    top: 0;
    width: 394px;
    height: 506px;
    background: var(--panel-veil);
    padding: 160px 0 0 32px;
  }
  .welcome-title {
    font-family: "Raleway", sans-serif;
    font-weight: 300;
    font-size: 35px;
    color: var(--accent-red);
    line-height: 1;
    margin-bottom: 27px;
  }
  .welcome-copy p {
    font-family: "Arimo", Helvetica, Arial, sans-serif;
    font-size: 13.4px;
    letter-spacing: -0.15px;
    line-height: 22.8px;
    color: var(--ink-navy);
    margin-bottom: 16px;
    white-space: nowrap;
  }
</style>
</head>
<body>
  <div class="site">
    <aside class="sidebar">
      <div class="brand">
        <span class="brand-mark"></span>
        <span class="brand-name">Venkira Interiors</span>
      </div>
      <ul class="main-nav">
        <li class="is-current">Home</li>
        <li>About us</li>
        <li>Our Services</li>
        <li>Products</li>
        <li>Gallery</li>
        <li>Contact Us</li>
      </ul>
      <div class="social-links" aria-label="Social media links">
        <span></span>
        <span></span>
      </div>
    </aside>

    <section class="hero">
      <div class="hero-photo" role="img" aria-label="Bright modern living room with a white sofa, grey cushions, pale wood floor and a glass partition to a dining area"></div>
      <div class="welcome-panel">
        <h1 class="welcome-title">Welcome</h1>
        <div class="welcome-copy">
          <p>With the various materials, colors, and finishes available<br>the choices today can be daunting. By listening to you, I<br>am able to pick just the right color, the right fabric, or<br>the right furniture for your projects.</p>
          <p>Whether you are starting with a small project or a large<br>project, I am ready to bring your ideas to life. It doesn't<br>take a big budget to achieve dramatic effects. A won-<br>derful new look is within anyone's reach.</p>
        </div>
      </div>
    </section>
  </div>
</body>
</html>
```